Business card design for Plumbing and Gas fitting company

We need a business card design for our plumbing and gas fitting company using the company logo and director details. Design should be modern and eye-catching however kept reasonably simple. This design should be targeted at commercial businesses/work so professionalism is key.

Target Market(s)

Commercial/business

Industry/Entity Type

Plumbing

Contact Information for Business Card

Warren Dohey
Director
027 581 9043
warren@vantorplumbingandgas.example
PO Box 7816
Palmerston North 4472

Font styles to use
Sans Serif

Requirements
Must have
• Logo
• Modern
• Kept simple
Nice to have
• Colour scheme based around logo

```html
<!DOCTYPE html>
<html lang="en">
<head>
<meta charset="utf-8">
<title>Vantor Plumbing &amp; Gas – Business Card</title>
<link href="https://fonts.googleapis.com/css2?family=Open+Sans:ital,wght@0,400;0,600;0,700;1,400&display=swap" rel="stylesheet">
<style>
  :root {
    --brand-blue: #0a6fbd;
    --brand-orange: #e8782f;
    --wave-light: #cfe2f3;
    --ink: #3d3d3d;
    --paper: #ffffff;
    --card-black: #050505;
    --backdrop: #e7e4df;
  }
  * { box-sizing: border-box; margin: 0; padding: 0; }
  html, body {
    width: 1200px; height: 987px; overflow: hidden;
    background: var(--backdrop);
    font-family: "Open Sans", sans-serif;
  }
  .card {
    position: absolute;
    left: 293px;
    width: 615px; height: 350px;
    border-radius: 17px;
    overflow: hidden;
  }
  .card--front { top: 131px; background: var(--paper); }
  .card--back { top: 506px; background: var(--card-black); }

  .card__waves { position: absolute; inset: 0; width: 100%; height: 100%; }

  .person {
    position: absolute; right: 35px; top: 22px;
    text-align: right; color: var(--paper);
  }
  .person__name { font-size: 21px; font-weight: 700; line-height: 1.25; }
  .person__role { font-size: 16px; font-weight: 400; line-height: 1.2; }

  .brand {
    position: absolute;
    display: flex; align-items: center; gap: 10px;
    font-weight: 700; color: var(--brand-blue);
    white-space: nowrap;
  }
  .brand__dot { border-radius: 50%; background: var(--brand-orange); flex: none; }
  .card--front .brand { left: 33px; top: 160px; font-size: 27px; }
  .card--front .brand__dot { width: 20px; height: 20px; }
  .card--back .brand { right: 35px; top: 272px; font-size: 23px; }
  .card--back .brand__dot { width: 16px; height: 16px; }

  .contact {
    position: absolute; left: 33px; top: 254px;
    list-style: none; color: var(--ink); font-size: 15px; line-height: 23px;
  }
  .contact li { display: flex; align-items: center; gap: 8px; }
  .contact svg { width: 14px; height: 14px; fill: var(--brand-blue); flex: none; }

  .address {
    position: absolute; right: 35px; top: 277px;
    text-align: right; color: var(--ink); font-size: 15px; line-height: 23px;
  }

  .web {
    position: absolute; right: 38px; top: 306px;
    color: var(--paper); font-size: 16px; font-style: italic;
  }
</style>
</head>
<body>

<section class="card card--front" aria-label="Business card front">
  <svg class="card__waves" viewBox="0 0 525 298" preserveAspectRatio="none" aria-hidden="true">
    <path d="M0,0 H525 V62 C470,80 420,88 360,76 C300,64 255,42 205,40 C110,36 30,80 0,130 Z" fill="var(--brand-blue)"/>
    <path d="M0,150 C25,95 110,35 245,58 C140,48 45,95 0,165 Z" fill="var(--brand-orange)"/>
    <path d="M230,60 C330,90 430,102 525,86 V96 C430,112 330,100 230,60 Z" fill="var(--brand-blue)"/>
  </svg>

  <div class="person">
    <p class="person__name">Warren Dohey</p>
    <p class="person__role">Director</p>
  </div>

  <div class="brand"><span>Vantor Plumbing &amp; Gas</span><span class="brand__dot"></span></div>

  <ul class="contact">
    <li><svg viewBox="0 0 24 24"><path d="M6.6 10.8a15.1 15.1 0 0 0 6.6 6.6l2.2-2.2c.3-.3.7-.4 1-.2 1.1.4 2.3.6 3.6.6.6 0 1 .4 1 1V20c0 .6-.4 1-1 1A17 17 0 0 1 3 4c0-.6.4-1 1-1h3.5c.6 0 1 .4 1 1 0 1.3.2 2.5.6 3.6.1.3 0 .7-.2 1z"/></svg>027 581 9043</li>
    <li><svg viewBox="0 0 24 24"><path d="M2 5h20v14H2z M3 6l9 7 9-7" stroke="#fff" stroke-width="1.5"/></svg>warren@vantorplumbingandgas.example</li>
    <li><svg viewBox="0 0 24 24"><circle cx="12" cy="12" r="10"/><path d="M2 12h20M12 2c3 3 3 17 0 20M12 2c-3 3-3 17 0 20" stroke="#fff" stroke-width="1.3" fill="none"/></svg>vantorplumbingandgas.example</li>
  </ul>

  <div class="address">
    <p>PO Box 7816</p>
    <p>Palmerston North 4472</p>
  </div>
</section>

<section class="card card--back" aria-label="Business card back">
  <div class="brand"><span>Vantor Plumbing &amp; Gas</span><span class="brand__dot"></span></div>
  <p class="web">vantorplumbingandgas.example</p>
</section>

</body>
</html>
```